Business card

creative business card for newly created national firm that specializes in high-density storage for retail markets. Looking for creativity and overall theme that will differentiate from others in this unique niche ...essentially a design that will provide instant recognition as we develop our identity in the marketplace. possible initial thoughts are attached with logo separately

Industry/Entity Type

Retail

```html
<!DOCTYPE html>
<html lang="en">
<head>
<meta charset="utf-8">
<title>Shelfwise Storage – Business Card</title>
<link rel="stylesheet" href="https://fonts.googleapis.com/css2?family=Questrial&display=swap">
<style>
  :root {
    --card-bg: #ffffff;
    --ink: #111111;
    --accent: #1fc3f2;
    --brand-faint: #e6eef3;
    --mark-faint: #e9edef;
  }
  html, body {
    margin: 0;
    padding: 0;
    width: 1200px;
    height: 686px;
    overflow: hidden;
    background: var(--card-bg);
  }
  .card {
    position: relative;
    width: 1200px;
    height: 686px;
    background: var(--card-bg);
    font-family: "Questrial", "Century Gothic", sans-serif;
    color: var(--ink);
  }
  .address {
    position: absolute;
    top: 66px;
    left: 0;
    width: 1204px;
    text-align: center;
    font-size: 34px;
    line-height: 52px;
    margin: 0;
    font-style: normal;
  }
  .address span { display: block; }
  .brand {
    position: absolute;
    top: 228px;
    left: 140px;
    display: flex;
    align-items: center;
    gap: 24px;
  }
  .brand-square {
    width: 110px;
    height: 110px;
    background: var(--mark-faint);
  }
  .brand-name {
    font-size: 108px;
    line-height: 96px;
    color: var(--brand-faint);
    letter-spacing: 2px;
    text-transform: uppercase;
  }
  .brand-name span { display: block; }
  .contact {
    position: absolute;
    top: 516px;
    left: 0;
    width: 1204px;
    text-align: center;
    font-size: 34px;
    line-height: 48px;
  }
  .contact-email { display: block; color: var(--accent); }
  .contact-web { display: block; color: var(--ink); }
</style>
</head>
<body>
  <main class="card">
    <address class="address">
      <span>Juniper Ridge Street Address Pinecrest, AZ 8888</span>
      <span>PO Box Number Pinecrest, AZ 9999</span>
    </address>

    <div class="brand">
      <div class="brand-square" aria-hidden="true"></div>
      <div class="brand-name">
        <span>Shelfwise</span>
        <span>Storage</span>
      </div>
    </div>

    <div class="contact">
      <span class="contact-email">contact@shelfwisestorage.com</span>
      <span class="contact-web">Online -- www.shelfwisestorage.com</span>
    </div>
  </main>
</body>
</html>
```